Landing Page für Persönlichkeitsquiz
Zielgruppe
Persönlichkeitsquiz für Menschen über 40 Jahren die bessere Entscheidungen treffen möchten.
Aufgabenstellung
Landinpage Design plus QUIZ ( 6 Schritte)
Vollständige Projektbeschreibung:
Projektbeschreibung
„Roaming Sideways QUIZ“
roamingsideways.example
- Responsive Design für mobile & website (Most users: mobile)
- Design wird Grundlage für spätere Website
Dieses Quiz wendet sich an Menschen über 40 Jahre, die ihre persönlichen Lebensziele besser erreichen möchten. Bitte denke daran, dass Menschen in unserem Alter schon schlechter sehen – also bitte eine gut lesbare & etwas größere Schrift verwenden!
Auftrag:
QUIZ mit mehreren Runden
Schritte des Quiz:
1. Landingpage
1.1 Video (youtube eingebunden)
1.2 Text
1.3 „Start Quiz“ Button
1.4 „Bekannt aus“ mit Logos von Medien in denen Marv Olden besprochen wurde.
1.5 Testimonials?
QUIZ (Popup)
2. Erste Runde: „Kille“ alle Antworten die Dich nicht interessieren. Total 64 Antworten.
2.1 Text mit Aufgabenbeschreibung „Kille“ alle Antworten die Dich nicht interessieren. Du hast zwei Minuten.“
2.2 Ein Button pro Antwort (wie bei Lernivo)
2.3 Zwei Buttons pro Reihe
2.4 Oben: Progress bar
2.5 Oben: Countdown clock, Restzeit: 2 Minuten
3. Zweite Runde: „Wähle max. 18 Antworten aus die überleben sollen.“
3.1 Text mit Aufgabenbeschreibung „Wähle max. 18 Antworten aus die überleben sollen.“
3.2 Ein Button pro Antwort (wie bei Lernivo)
3.3 Zwei Buttons pro Reihe
3.4 Oben: Progress bar
3.5 Oben: Countdown clock, Restzeit: 60 Sekunden
3.6 Zähler der noch verfügbaren Antworten. Hier: Noch 18, noch 17, noch 16.. etc.
4. Dritte Runde: „Nur 9 Antworten dürfen überleben. Go!“
4.1 Text mit „Nur 9 Antworten dürfen überleben. Go!“
4.2 Ein Button pro Antwort (wie bei Lernivo)
4.3 Zwei Buttons pro Reihe
4.4 Oben: Progress bar
4.5 Oben: Countdown clock, Restzeit 45 ..

```html
<!DOCTYPE html>
<html lang="de">
<head>
<meta charset="utf-8">
<title>Roaming Sideways QUIZ – Ziel erreicht</title>
<link href="https://fonts.googleapis.com/css2?family=Open+Sans:wght@400;600;700&display=swap" rel="stylesheet">
<style>
:root{
  --hero-a:#4a1aa3;
  --hero-b:#2f0f8e;
  --band:#6a3cc0;
  --band-dark:#5a34b2;
  --footer:#3a1592;
  --dim-text:#8a66db;
  --dim-btn:#6b3a7c;
  --dim-btn-text:#a877e6;
  --white:#ffffff;
  --ink:#333333;
  --muted:#666666;
  --violet:#b05ad6;
  --gold:#e8b33f;
  --blue:#6b8fe0;
  --green:#5cbf4e;
  --pink:#f28fc6;
  --field:#ebebeb;
}
*{box-sizing:border-box;margin:0;padding:0}
html,body{width:864px;height:1200px;overflow:hidden}
body{position:relative;font-family:"Open Sans",Arial,sans-serif;background:var(--band);color:var(--ink)}
.abs{position:absolute}

/* page behind the dialog */
.hero{left:0;top:0;width:864px;height:409px;background:linear-gradient(120deg,var(--hero-a),var(--hero-b))}
.brand{left:63px;top:40px;font-size:12.5px;font-weight:600;line-height:17px;color:var(--dim-text);letter-spacing:.3px}
.lang{left:718px;top:58px;width:16px;height:16px;border-radius:50%;background:linear-gradient(#1a1230 33%,#8a2030 33% 66%,#b08a30 66%)}
.lang-caret{left:740px;top:62px}
.nav-link{left:770px;top:59px;font-size:10px;color:var(--dim-text)}
.hero-title{left:63px;top:143px;font-size:19px;font-weight:700;line-height:26px;color:var(--dim-text);white-space:nowrap}
.hero-copy{left:63px;top:205px;font-size:9.5px;line-height:13px;color:var(--dim-text);white-space:nowrap}
.btn-dim{background:var(--dim-btn);color:var(--dim-btn-text);border-radius:14px;font-size:9.5px;font-weight:700;display:flex;align-items:center;justify-content:center;gap:4px;padding:0;white-space:nowrap;line-height:1}
.hero-btn{left:63px;top:260px;width:93px;height:27px}
.hero-visual{left:739px;top:107px;width:61px;height:201px;background:#6a2aa8}
.hero-dot{left:730px;top:86px;width:28px;height:28px;border-radius:50%;background:#4a20a8}
.media-band{left:0;top:409px;width:864px;height:208px;background:var(--band)}
.media-tile{top:490px;width:32px;height:55px;background:#0a0a18}
.media-tile.right{left:740px;top:500px;width:36px;height:36px}
.arrow-dim{width:13px;height:13px;border-radius:50%;background:var(--dim-btn)}
.deco-circle{border-radius:50%;background:linear-gradient(160deg,#3a16a0,#28108a)}
.testimonials{left:0;top:617px;width:864px;height:261px;background:var(--band-dark)}
.testimonial-card{left:63px;top:698px;width:737px;height:112px;background:#6a42c0;border-bottom:3px solid #7a3fc8}
.avatar{left:75px;top:711px;width:49px;height:49px;border-radius:50%;background:radial-gradient(circle at 40% 40%,#8a5a7a,#4a2a5a)}
.testimonial-text{font-size:8px;line-height:11px;color:var(--dim-text);white-space:nowrap}
.about{left:0;top:878px;width:864px;height:286px;background:var(--band)}
.section-title{font-size:11px;font-weight:700;text-align:center;left:0;width:864px;white-space:nowrap}
.rule{width:30px;height:2px;background:var(--violet);left:417px}
.about-title{top:902px;color:#2a1060}
.about-rule{top:923px;background:#7a3fc8}
.about-photo{left:113px;top:952px;width:146px;height:146px;border-radius:50%;background:linear-gradient(135deg,#8a6ad8,#3a2470)}
.about-dot{left:78px;top:1074px;width:40px;height:40px;border-radius:50%;background:linear-gradient(#3a16a0,#2a0f8a)}
.about-head{left:312px;top:952px;font-size:11px;font-weight:700;color:#2a1060}
.about-copy{left:312px;top:983px;width:478px;font-size:8px;line-height:10.8px;color:#2e1868}
.about-copy p{margin-bottom:10.6px}
.about-btn{left:312px;top:1095px;width:93px;height:27px}
.footer{left:0;top:1164px;width:864px;height:36px;background:var(--footer);font-size:8px;color:#5a3ac0}
.footer span{position:absolute;top:13px;white-space:nowrap}

/* dialog */
.dialog{left:125px;top:83px;width:614px;height:757px;background:var(--white);border-bottom:4px solid var(--violet)}
.badge{left:419px;top:70px;width:26px;height:26px;border-radius:50%;background:var(--violet);border:2px solid var(--white);display:flex;align-items:center;justify-content:center}
.back{left:148px;top:99px;display:flex;align-items:center;gap:5px;font-size:10px;font-weight:700;color:var(--gold)}
.round-arrow{width:13px;height:13px;border-radius:50%;background:var(--gold);display:flex;align-items:center;justify-content:center}
.dialog-title{left:125px;width:614px;top:100px;text-align:center;font-size:11px;color:#555}
.close{left:652px;top:99px;display:flex;align-items:center;gap:6px;font-size:10px;font-weight:700;color:var(--violet);white-space:nowrap}
.video{left:148px;top:131px;width:568px;height:159px;background:linear-gradient(90deg,#f29acb,#f08cc4 50%,#f29acb)}
.play{left:419px;top:200px;width:26px;height:26px;border-radius:50%;background:var(--white);display:flex;align-items:center;justify-content:center}
.dlg-title{top:314px;color:#333}
.dlg-rule-1{top:333px}
.lead{left:125px;width:614px;top:344px;text-align:center;font-size:11px;color:#555}
.values{left:125px;width:614px;top:381px;display:flex;justify-content:center;gap:9px}
.value{height:27px;width:106px;border-radius:14px;display:flex;align-items:center;gap:5px;padding-left:7px;color:var(--white);font-size:11.2px;font-weight:700;white-space:nowrap}
.value.gold{background:var(--gold)} .value.blue{background:var(--blue)} .value.green{background:var(--green)}
.body-copy{left:148px;width:568px;top:427px;text-align:center;font-size:9.6px;line-height:13.95px;color:#5a5a5a}
.body-copy p+p{margin-top:14px}
.nl-title{top:618px;color:#333}
.dlg-rule-2{top:640px}
.field{top:660px;height:27px;border-radius:14px;background:var(--field);font-size:9.5px;color:#777;padding-left:16px;display:flex;align-items:center}
.field.name{left:148px;width:180px}
.field.mail{left:335px;width:270px;padding-left:14px}
.send{left:615px;top:660px;width:93px;height:27px;border-radius:14px;background:var(--gold);color:var(--white);font-size:9.5px;font-weight:700;display:flex;align-items:center;justify-content:center;gap:4px;white-space:nowrap}
.press-title{top:717px;color:#333}
.dlg-rule-3{top:739px}
.press-arrow{top:769px}
.press-row{left:166px;width:532px;top:754px;height:43px;display:flex;align-items:center;justify-content:space-between}
.press-name{font-size:10.5px;font-weight:700;color:#111;display:flex;align-items:center;gap:4px;white-space:nowrap}
.press-name i{display:block;width:8px;height:8px;background:#111}
.below-btn{left:385px;top:834px;width:94px;height:26px}
</style>
</head>
<body>

<div class="abs hero"></div>
<div class="abs brand">ROAMING<br>SIDEWAYS</div>
<div class="abs lang" role="img" aria-label="Sprache Deutsch"></div>
<svg class="abs lang-caret" width="9" height="6" viewBox="0 0 9 6"><path d="M1 1l3.5 3.5L8 1" fill="none" stroke="#6a50c8" stroke-width="1.2"/></svg>
<div class="abs nav-link">Fragen</div>
<div class="abs hero-dot"></div>
<div class="abs hero-visual" role="img" aria-label="Illustration im Kopfbereich"></div>
<div class="abs hero-title">Herzlich willkommen<br>bei Roaming Sideways</div>
<div class="abs hero-copy">Lorem ipsum dolor sit amet, consetetur<br>nonumy eirmod tempor invidunt ut<br>aliquyam erat, sed diam voluptua.</div>
<div class="abs btn-dim hero-btn">→ Quiz starten</div>

<div class="abs media-band"></div>
<div class="abs arrow-dim" style="left:63px;top:512px"></div>
<div class="abs media-tile" style="left:93px"></div>
<div class="abs media-tile right"></div>
<div class="abs arrow-dim" style="left:788px;top:511px"></div>
<div class="abs deco-circle" style="left:832px;top:432px;width:120px;height:120px"></div>

<div class="abs testimonials"></div>
<div class="abs deco-circle" style="left:-90px;top:655px;width:124px;height:134px"></div>
<div class="abs testimonial-card"></div>
<div class="abs avatar" role="img" aria-label="Porträtfoto einer Teilnehmerin"></div>
<div class="abs testimonial-text" style="left:75px;top:767px">Lorem ipsum dolor sit amet,<br>sed diam nonumy eirmod<br>dolore magna aliquyam.</div>
<div class="abs testimonial-text" style="left:735px;top:767px">psing elitr,<br>t labore et<br>tua.</div>
<svg class="abs" style="left:776px;top:707px" width="14" height="14" viewBox="0 0 14 14"><path d="M7 1.5a5.5 5 0 1 1-3 9.2L1.5 12l.9-2.8A5 5 0 0 1 7 1.5z" fill="none" stroke="#7a4fd0" stroke-width="1.1"/></svg>

<div class="abs about"></div>
<div class="abs section-title about-title">Über MarvOlden</div>
<div class="abs rule about-rule"></div>
<div class="abs about-photo" role="img" aria-label="Foto von Marv Olden mit Partnerin"></div>
<div class="abs about-dot"></div>
<div class="abs about-head">Was meine Oma mich lehrte</div>
<div class="abs about-copy">
  <p>Die einflussreichste Person in meinem Leben war meine Großmutter. Sie wurde im Deutschen Kaiserreich geboren; erlebte zwei Weltkriege, die Mondlandung und Fensterwerk 95.</p>
  <p>Während des Krieges ging sie nach Dresden, um ihre Tochter aus der “Landverschickung” nach Hause zu holen, und zwang die Schulleiterin, ihre Tochter zurückzugeben. Dann brachte Oma sie (die Tochter, nicht die Schulleiterin) durch halb Deutschland und das ganze Chaos des zerstörten Eisenbahnnetzes nach Hause. Dresden wurde in der nächsten Nacht bombardiert, meine Mutter hätte das nicht überlebt.</p>
  <p>Meine Großmutter lehrte mich, Menschen nach ihren Taten zu beurteilen, nicht nach ihren Worten.</p>
</div>
<div class="abs btn-dim about-btn">→ Quiz starten</div>

<div class="abs footer">
  <span style="left:63px">© Roaming Sideways QUIZ</span>
  <span style="left:634px">Impressum</span>
  <span style="left:700px">Datenschutz</span>
  <span style="left:767px">Sitemap</span>
</div>

<div class="abs btn-dim below-btn">→ Quiz starten</div>

<div class="abs dialog"></div>
<div class="abs badge">
  <svg width="14" height="14" viewBox="0 0 24 24"><path d="M12 2.5l2.9 6.2 6.6.7-5 4.5 1.4 6.6L12 17.2l-5.9 3.3 1.4-6.6-5-4.5 6.6-.7z" fill="none" stroke="#fff" stroke-width="1.8" stroke-linejoin="round"/></svg>
</div>
<div class="abs back"><span class="round-arrow"><svg width="6" height="8" viewBox="0 0 6 8"><path d="M4.5 1L1.5 4l3 3" fill="none" stroke="#fff" stroke-width="1.4"/></svg></span>zurück</div>
<div class="abs dialog-title">Ziel erreicht!</div>
<div class="abs close">Schließen <svg width="9" height="9" viewBox="0 0 9 9"><path d="M1 1l7 7M8 1L1 8" stroke="#b05ad6" stroke-width="2"/></svg></div>

<div class="abs video" role="img" aria-label="Videovorschau: gezeichnete Figur mit Blumen und erhobener Hand auf rosa Grund"></div>
<div class="abs play"><svg width="10" height="11" viewBox="0 0 10 11"><path d="M2 1l7 4.5L2 10z" fill="#f08cc4"/></svg></div>

<div class="abs section-title dlg-title">Deine Werte</div>
<div class="abs rule dlg-rule-1"></div>
<div class="abs lead">Hier sind Deine Top drei Werte und sortiert nach deiner persönlichen Wichtigkeit.</div>
<div class="abs values">
  <div class="value gold"><svg width="15" height="15" viewBox="0 0 24 24"><path d="M12 2.5l2.9 6.2 6.6.7-5 4.5 1.4 6.6L12 17.2l-5.9 3.3 1.4-6.6-5-4.5 6.6-.7z" fill="none" stroke="#fff" stroke-width="1.8" stroke-linejoin="round"/></svg>Abenteurer</div>
  <div class="value blue"><svg width="15" height="15" viewBox="0 0 24 24"><path d="M12 2.5l2.9 6.2 6.6.7-5 4.5 1.4 6.6L12 17.2l-5.9 3.3 1.4-6.6-5-4.5 6.6-.7z" fill="none" stroke="#fff" stroke-width="1.8" stroke-linejoin="round"/></svg>Disiplinierter</div>
  <div class="value green"><svg width="15" height="15" viewBox="0 0 24 24"><path d="M12 2.5l2.9 6.2 6.6.7-5 4.5 1.4 6.6L12 17.2l-5.9 3.3 1.4-6.6-5-4.5 6.6-.7z" fill="none" stroke="#fff" stroke-width="1.8" stroke-linejoin="round"/></svg>Offener Typ</div>
</div>

<div class="abs body-copy">
  <p>Lorem ipsum dolor sit amet, consetetur sadipscing elitr, sed diam nonumy eirmod tempor invidunt ut labore et dolore magna aliquyam erat, sed diam voluptua. At vero eos et accusam et justo duo dolores et ea rebum. Stet clita kasd gubergren, no sea takimata sanctus est Lorem ipsum dolor sit amet. Lorem ipsum dolor sit amet, consetetur sadipscing elitr, sed diam nonumy eirmod tempor invidunt ut labore et dolore magna aliquyam erat, sed diam voluptua. At vero eos et accusam et justo duo dolores et ea rebum. Stet clita kasd gubergren, no sea takimata sanctus est Lorem ipsum dolor sit amet. Lorem ipsum dolor sit amet, consetetur sadipscing elitr, sed diam nonumy eirmod tempor invidunt ut labore et dolore magna aliquyam erat, sed diam voluptua. At vero eos et accusam et justo duo dolores et ea rebum. Stet clita kasd gubergren, no sea takimata sanctus est Lorem ipsum dolor sit amet.</p>
  <p>Duis autem vel eum iriure dolor in hendrerit in vulputate velit esse molestie consequat, vel illum dolore eu feugiat nulla facilisis at vero eros et accumsan et iusto odio dignissim qui blandit praesent luptatum zzril delenit augue duis dolore te feugait nulla facilisi. Lorem ipsum dolor sit amet,</p>
</div>

<div class="abs section-title nl-title">Newsletter abonieren</div>
<div class="abs rule dlg-rule-2"></div>
<div class="abs field name">Deine Name</div>
<div class="abs field mail">E-Mail-Adresse</div>
<div class="abs send">→ Jetzt senden</div>

<div class="abs section-title press-title">Bekannt aus</div>
<div class="abs rule dlg-rule-3"></div>
<div class="abs round-arrow press-arrow" style="left:147px"><svg width="6" height="8" viewBox="0 0 6 8"><path d="M4.5 1L1.5 4l3 3" fill="none" stroke="#fff" stroke-width="1.4"/></svg></div>
<div class="abs press-row">
  <span class="press-name"><i></i>Nordfunk</span>
  <span class="press-name">Tagesblatt</span>
  <span class="press-name">Radio Elf</span>
  <span class="press-name">Europost</span>
  <span class="press-name">Welle Drei</span>
  <span class="press-name">Westfunk</span>
  <span class="press-name"><i></i>Zeitkanal</span>
</div>
<div class="abs round-arrow press-arrow" style="left:703px"><svg width="6" height="8" viewBox="0 0 6 8"><path d="M1.5 1l3 3-3 3" fill="none" stroke="#fff" stroke-width="1.4"/></svg></div>

</body>
</html>
```